Webdesign für IT-Beratungsdienstleister
Zielgruppe
7K-ADVISA ist spezialisiert auf Fach- und IT-Beratungsdienstleistungen.
Wir unterstützen Unternehmen bei der Leistungsoptimierung durch prozessgetriebene Informationssysteme und Integrationslösungen.
Bitte siehe Aufgaben hier: http://www.7k-advisa.example/ueber-uns/
Zielgruppe sind Mittelständige und sowie Grossunternehmen
Aufgabenstellung
Wordpress template, modern, nicht zu überladen mit der Möglichkeit Beiträge zu veröffentlicehn. Responsive.

```html
<!DOCTYPE html>
<html lang="de">
<head>
<meta charset="utf-8">
<title>7K-ADVISA – Fach- und IT-Beratung</title>
<link rel="stylesheet" href="https://fonts.googleapis.com/css2?family=Ubuntu:wght@300;400;500;700&family=Open+Sans:wght@400;600;700&display=swap">
<style>
:root{
  --orange:#e8680f;
  --red:#e3261b;
  --ink:#333;
  --muted:#666;
  --line:#e2e2e2;
  --navy:#2a3140;
  --footer:#2b303b;
  --white:#fff;
}
*{margin:0;padding:0;box-sizing:border-box}
html,body{width:1200px;height:2386px;overflow:hidden}
body{font-family:"Open Sans",Arial,sans-serif;color:var(--ink);background:var(--white);position:relative}
.wrap{position:absolute;left:240px;width:720px}

/* header */
.site-header{position:absolute;top:0;left:0;width:1200px;height:63px;background:var(--white);border-bottom:1px solid #eee}
.brand{position:absolute;left:245px;top:14px;font-family:"Ubuntu",sans-serif;font-size:30px;font-weight:400;color:#222;letter-spacing:1px}
.main-nav{position:absolute;right:248px;top:22px;display:flex;gap:18px;font-family:"Ubuntu",sans-serif;font-size:11px;font-weight:300;color:#555}
.main-nav a{color:inherit;text-decoration:none;line-height:18px}
.main-nav .active{color:var(--orange);border:1px solid var(--orange);padding:0 7px}

/* hero */
.hero{position:absolute;top:63px;left:0;width:1200px;height:297px;background:linear-gradient(100deg,#6f9bb1 0%,#8fb4c3 35%,#9fbcbe 55%,#4e6f87 80%,#3d5a70 100%)}
.hero-photo{position:absolute;right:40px;top:0;width:560px;height:297px;background:radial-gradient(ellipse at 55% 60%,#d8d9d2 0 18%,#2b3450 35%,rgba(43,52,80,0) 62%)}
.hero-text{position:absolute;left:151px;top:70px;width:410px;color:var(--white)}
.hero-text h1{font-family:"Ubuntu",sans-serif;font-weight:400;font-size:18px}
.rule{display:block;width:32px;height:2px;background:var(--red);margin:11px 0 19px}
.hero-text p{font-family:"Ubuntu",sans-serif;font-size:12.5px;line-height:14px;margin-bottom:10px}
.btn-outline{display:inline-block;border:1.5px solid var(--white);color:var(--white);font-size:9px;font-weight:700;padding:5px 20px;margin-top:8px}
.slider-arrow{position:absolute;top:136px;width:25px;height:25px;background:rgba(255,255,255,.35);border:1px solid rgba(255,255,255,.6)}
.slider-arrow.prev{left:12px}.slider-arrow.next{right:12px}
.dots{position:absolute;top:275px;left:579px;display:flex;gap:4px}
.dots i{width:7px;height:7px;border-radius:50%;background:#222;border:1px solid #fff}
.dots i:first-child{background:#fff}

/* services */
.service{position:absolute;top:423px;width:220px;height:310px;border:1px solid var(--line);border-bottom:none;text-align:center}
.service h3{font-family:"Ubuntu",sans-serif;font-weight:400;font-size:13px;color:#444;margin-top:8px}
.service .art{width:126px;height:126px;border-radius:50%;margin:13px auto 14px;background:radial-gradient(circle at 50% 55%,#e9e2d8 0 30%,var(--orange) 31%)}
.service p{font-size:10px;line-height:15px;color:var(--muted);padding:0 11px}
.s1{left:250px}.s2{left:489px}.s3{left:729px}
.s2 h3,.s3 h3{margin-top:15px}
.s2 .art{background:radial-gradient(circle at 50% 50%,#6d7f8c 0 44%,var(--orange) 45%)}
.s3 .art{background:linear-gradient(#0fa27f,#0fa27f) center 40%/78px 54px no-repeat,var(--orange)}

/* about */
.about{position:absolute;top:789px;left:0;width:1200px;height:312px;background:linear-gradient(90deg,#232a38 0%,#343d50 40%,#4b5568 70%,#5b6577 100%)}
.about-text{position:absolute;left:548px;top:62px;width:410px;color:var(--white)}
.about-text h2{font-family:"Ubuntu",sans-serif;font-weight:400;font-size:18px}
.about-text p{font-family:"Ubuntu",sans-serif;font-size:12.5px;line-height:16.5px}
.about-text .btn-outline{margin-top:20px;padding:5px 13px}

/* articles */
.articles-title{position:absolute;top:1138px;left:0;width:1200px;text-align:center;font-family:"Ubuntu",sans-serif;font-weight:300;font-size:19px;color:#333}
.articles-title .rule{margin:9px auto 0}
.carousel-nav{position:absolute;top:1189px;left:939px;font-size:12px;color:var(--orange);letter-spacing:4px}
.article{position:absolute;top:1205px;width:227px}
.a1{left:247px}.a2{left:487px}.a3{left:726px}
.thumb{height:129px;background:linear-gradient(135deg,#5a5f66,#2c3038 60%,#3d4047);border:1px solid #ccc}
.read-more{position:absolute;left:-7px;top:99px;background:var(--red);color:var(--white);font-size:7px;font-weight:700;padding:5px 9px}
.meta{font-size:6px;font-style:italic;color:#888;margin-top:17px}
.meta span{color:var(--orange)}
.article h4{font-size:10px;font-style:italic;font-weight:400;color:var(--orange);margin-top:8px}
.btn-orange{position:absolute;top:1410px;left:558px;width:84px;height:26px;background:var(--orange);color:var(--white);font-size:8px;font-weight:700;text-align:center;line-height:26px}

/* contact */
.contact-band{position:absolute;top:1481px;left:0;width:1200px;height:344px;background:linear-gradient(#6c7680 0%,#5f6a6a 30%,#3d4a33 60%,#2f3b29 100%)}
.callout{position:absolute;left:241px;top:105px;width:718px;height:125px}
.callout-text{position:absolute;left:31px;top:48px;color:var(--white)}
.callout-text h3{font-family:"Ubuntu",sans-serif;font-weight:300;font-size:15px}
.callout-text p{font-family:"Ubuntu",sans-serif;font-size:9px;color:#fbd7b8;margin-top:11px}
.callout .btn-outline{position:absolute;left:573px;top:64px;margin:0;padding:4px 13px;font-size:8px}

/* map */
.map{position:absolute;top:1825px;left:0;width:1200px;height:315px;background:linear-gradient(120deg,#fde7d6,#fbc9a3 40%,#fde2cc 70%,#f8bf95)}
.map-controls{position:absolute;left:6px;top:12px;background:#fff;font-size:6px;padding:4px 6px;box-shadow:0 1px 2px rgba(0,0,0,.3)}
.zoom{position:absolute;left:6px;top:148px;width:17px;height:34px;background:#fff;box-shadow:0 1px 2px rgba(0,0,0,.3);font-size:11px;text-align:center;line-height:16px}
.map-status{position:absolute;left:19px;top:246px;background:#fff;font-size:9px;padding:4px 6px}

/* footer */
.site-footer{position:absolute;top:2140px;left:0;width:1200px;height:246px;background:var(--footer);color:var(--white)}
.footer-brand{position:absolute;left:245px;top:26px;font-family:"Ubuntu",sans-serif;font-size:22px;color:var(--white)}
.footer-about{position:absolute;left:240px;top:92px;width:285px;font-size:6.5px;font-weight:600;line-height:15.5px}
.footer-col h5{font-size:10px;font-weight:700;letter-spacing:.5px}
.links{position:absolute;left:548px;top:30px}
.links li{list-style:none;font-size:7px;font-weight:700;line-height:15.7px}
.links ul{margin-top:6px}
.social{position:absolute;left:793px;top:30px}
.social ul{margin-top:8px;margin-left:7px}
.social li{list-style:none;width:18px;height:17px;background:#111;border:1px solid #444;margin-bottom:5px}
.footer-rule{position:absolute;left:241px;top:183px;width:718px;height:2px;background:var(--red)}
.copyright{position:absolute;top:210px;left:0;width:1200px;text-align:center;font-size:8.5px;color:#aab}
.copyright b{color:var(--white)}
</style>
</head>
<body>

<header class="site-header">
  <div class="brand">7K-ADVISA</div>
  <nav class="main-nav">
    <a class="active">Home</a><a>Über Uns</a><a>Business Consulting</a><a>IT Consulting</a><a>Training</a><a>Kontakt</a>
  </nav>
</header>

<section class="hero">
  <div class="hero-photo" role="img" aria-label="Foto: Geschäftsmann öffnet sein Hemd vor blauem Himmel, darunter ein Shirt mit Firmenname"></div>
  <div class="hero-text">
    <h1>7K-ADVISA - Unser Know-How für Ihren Erfolg!</h1>
    <span class="rule"></span>
    <p>Wir beraten namhafte Unternehmen und stellen individuelle Lösungen zur Verfügung.</p>
    <p>Was dürfen wir für Sie tun?</p>
    <span class="btn-outline">Jetzt kontakt aufnehmen</span>
  </div>
  <span class="slider-arrow prev"><svg width="25" height="25" viewBox="0 0 25 25"><path d="M14 8l-4 4.5 4 4.5" fill="none" stroke="#fff" stroke-width="1.2"/></svg></span>
  <span class="slider-arrow next"><svg width="25" height="25" viewBox="0 0 25 25"><path d="M11 8l4 4.5-4 4.5" fill="none" stroke="#fff" stroke-width="1.2"/></svg></span>
  <div class="dots"><i></i><i></i><i></i><i></i></div>
</section>

<article class="service s1">
  <h3>Business Consulting</h3>
  <div class="art" role="img" aria-label="Illustration: Gruppe von Beratern"></div>
  <p>Wir unterstützen fachlich Ihre Prozessoptimierungsprojekte mit erstklassiger Beratung für Prozessmanagement, -analyse sowie -implementierung. Wir begleiten Sie bei dem Anforderungsmanagement, Business Analyse und Projektqualifizierung.</p>
</article>
<article class="service s2">
  <h3>IT Consulting</h3>
  <div class="art" role="img" aria-label="Illustration: Arbeitstisch mit Geräten von oben"></div>
  <p>Wir beraten und setzen die IT für Sie um: Technische Prozessimplementierung, Enterprise Architecture, Integration sowie SOA und JEE stellen unsere Kompetenzen dar. Wir bitten customizing von Unternehmenslösungen wie ERP, CRM, SCM an.</p>
</article>
<article class="service s3">
  <h3>Training &amp; Coaching</h3>
  <div class="art" role="img" aria-label="Illustration: Tafel mit Schulungsskizze"></div>
  <p>Auch Querschnittsthemen verlangen eine große Aufmerksamkeit. Wir leisten Unterstützung für Projektmanagement, und diverse Themen wie BPM Methodik &amp; Competence Center, BPMN, SOA, Enterprise Architecture als Berater, Coach, Trainer oder Interimmanager.</p>
</article>

<section class="about" role="img" aria-label="Hintergrundfoto: abgedunkeltes Büro">
  <div class="about-text">
    <h2>Über Uns</h2>
    <span class="rule"></span>
    <p>7K-ADVISA ist spezialisiert auf Fach- und IT-Beratungsdienstleistungen. Wir unterstützen Unternehmen bei der Leistungsoptimierung durch prozessgetriebene Informationssysteme. Unsere Kunden vertrauen unseren Full-Service Ansatz, der sich durch hohe Expertise mit fundierten Branchenübergreifenden Erfahrungen sowie Kompetenzen auszeichnet.</p>
    <span class="btn-outline">Mehr erfahren</span>
  </div>
</section>

<h2 class="articles-title">Letzte Artikeln<span class="rule"></span></h2>
<div class="carousel-nav">‹›</div>
<article class="article a1">
  <div class="thumb" role="img" aria-label="Foto: Schreibtisch mit Tastatur"></div>
  <span class="read-more">Read more +</span>
  <p class="meta">26. November 2016 Von admin in <span>Artikeln</span></p>
  <h4>MusterArtikel</h4>
</article>
<article class="article a2">
  <div class="thumb" role="img" aria-label="Foto: Schreibtisch mit Tastatur"></div>
  <span class="read-more">Read more +</span>
  <p class="meta">26. Oktober 2016 Von admin in <span>Artikeln</span></p>
  <h4>MusterArtikel</h4>
</article>
<article class="article a3">
  <div class="thumb" role="img" aria-label="Foto: Schreibtisch mit Tastatur"></div>
  <span class="read-more">Read more +</span>
  <p class="meta">26. September 2016 Von admin in <span>Artikeln</span></p>
  <h4>MusterArtikel</h4>
</article>
<div class="btn-orange">Ältere Artikeln</div>

<section class="contact-band" role="img" aria-label="Unscharfes Foto: Stadt mit Fernsehturm und Wald">
  <div class="callout">
    <svg width="718" height="140" viewBox="0 0 718 140" style="position:absolute;left:0;top:0">
      <path d="M0 0 L718 18 L718 125 L170 125 L160 134 L155 125 L0 125 Z" fill="#e8680f"/>
    </svg>
    <div class="callout-text">
      <h3>Wir freuen uns immer, von Ihnen zu hören.</h3>
      <p>Inhaber und Ansprechpartner: Dr. Lukas Verenholt</p>
    </div>
    <span class="btn-outline">Kontakt aufnehmen</span>
  </div>
</section>

<section class="map" role="img" aria-label="Karte: Stadtplan mit Standortmarkierung">
  <div class="map-controls">Karte &nbsp; Satellit</div>
  <div class="zoom">+<br>−</div>
  <div class="map-status">Verbindung finden...</div>
</section>

<footer class="site-footer">
  <div class="footer-brand">7K-ADVISA</div>
  <p class="footer-about">Lorem ipsum dolor sit amet, consetetur sadipscing elitr, sed diam nonumy eirmod tempor invidunt ut labore et dolore magna aliquyam erat, sed diam voluptua. At vero eos et accusam et justo duo dolores et ea rebum.</p>
  <div class="footer-col links">
    <h5>Links</h5>
    <ul><li>Home</li><li>Über Uns</li><li>Business Consulting</li><li>IT Consulting</li><li>Training</li><li>Kontakt</li></ul>
  </div>
  <div class="footer-col social">
    <h5>Soziale Netzwerke</h5>
    <ul>
      <li role="img" aria-label="Soziales Netzwerk 1"></li>
      <li role="img" aria-label="Soziales Netzwerk 2"></li>
      <li role="img" aria-label="Soziales Netzwerk 3"></li>
      <li role="img" aria-label="Soziales Netzwerk 4"></li>
      <li role="img" aria-label="Soziales Netzwerk 5"></li>
    </ul>
  </div>
  <div class="footer-rule"></div>
  <p class="copyright">Copyright © 2016 7K-ADVISA. | <b>Home</b> | <b>Impressum</b> | <b>Kontakt</b></p>
</footer>

</body>
</html>
```